Dynamic Business Card for Sports Supplements Company

Hi! I'm looking for an awesome business card to match my existing sports supplement company. I have uploaded my current company logo and screenshot of the front page of my website.

I would like to have something dynamic and interesting and utilize the colors in the website - the reds and purples

The business card should be double sided and focus on a unique eye-catching design on the back and include all the relevant company info.

Most importantly, it should say somewhere: "Sign up on our website for a coupon code."

Target Market(s)

Mostly for women gym goers but it shouldn't be too feminine. It should be in keeping with the website design. It should flow and clearly be connected to it

Industry/Entity Type

Business

Contact Information for Business Card

Lorena K. Vasquez
CEO
LVasquez@Fortivanco.example
www.fortivanco.example
614.275.3081
P.O. Box 48317
Dayton, Ohio 22417

Sign up on our website for a coupon code

Font styles to use
Serif
Sans Serif
Other font styles liked:
• Novecento font family and "Fortivan" is in AR Destine font

Requirements
Must have
• One side should be a bold Fortivan logo design. Even just the symbol itself may be o.k. (see attached file)

```html
<!DOCTYPE html>
<html lang="en">
<head>
<meta charset="utf-8">
<title>Fortivan Business Card</title>
<link rel="stylesheet" href="https://fonts.googleapis.com/css2?family=Open+Sans:ital,wght@0,400;0,700;1,400&display=swap">
<style>
  :root {
    --purple: #5e4680;
    --red: #e3232c;
    --white: #ffffff;
    --ink: #4a3a66;
    --backdrop: #6d7477;
  }
  * { margin: 0; padding: 0; box-sizing: border-box; }
  html, body {
    width: 1200px; height: 900px; overflow: hidden;
    background: var(--backdrop);
    font-family: "Open Sans", Arial, sans-serif;
  }
  .card {
    position: absolute; left: 290px;
    width: 620px; height: 354px;
    overflow: hidden;
    box-shadow: 0 10px 30px rgba(0,0,0,.35);
  }
  .card-front { top: 56px; background: var(--white); }
  .card-back { top: 490px; background: var(--purple); }

  .front-shapes { position: absolute; inset: 0; width: 620px; height: 354px; }

  .brand {
    position: absolute; left: 0; right: 0; top: 40px;
    display: flex; align-items: center; justify-content: center; gap: 14px;
  }
  .brand-mark { width: 30px; height: 30px; background: var(--red); }
  .brand-name {
    font-weight: 700; font-size: 40px; letter-spacing: 2px;
    color: var(--purple); text-transform: uppercase; line-height: 1;
  }
  .brand-tagline {
    position: absolute; left: 0; right: 0; top: 90px; text-align: center;
    font-size: 12px; color: var(--purple); letter-spacing: 1px;
  }

  .contact-list {
    position: absolute; left: 54px; top: 130px;
    list-style: none; font-size: 14px; color: var(--ink); line-height: 22px;
  }
  .contact-list li { display: flex; align-items: center; gap: 10px; }
  .contact-list svg { width: 12px; height: 12px; flex: none; }

  .person { position: absolute; left: 390px; top: 150px; }
  .person-name { font-size: 20px; color: var(--red); line-height: 26px; }
  .person-role { font-size: 12px; color: var(--ink); }

  .coupon-note {
    position: absolute; left: 40px; top: 314px;
    font-size: 14px; font-style: italic; color: var(--white); line-height: 20px;
  }
  .address {
    position: absolute; right: 50px; top: 276px;
    font-size: 15px; font-style: normal; color: var(--white);
    line-height: 22px; text-align: right;
  }

  .back-lockup {
    position: absolute; inset: 0;
    display: flex; flex-direction: column; align-items: center; justify-content: center;
    color: var(--white);
  }
  .back-name {
    font-weight: 700; font-size: 78px; letter-spacing: 4px;
    text-transform: uppercase; line-height: 1;
  }
  .back-tagline { font-size: 22px; letter-spacing: 3px; margin-top: 10px; }
</style>
</head>
<body>

<section class="card card-front" aria-label="Business card front">
  <svg class="front-shapes" viewBox="0 0 620 354" aria-hidden="true">
    <rect x="0" y="294" width="620" height="60" fill="var(--purple)"/>
    <polygon points="200,294 614,224 620,224 620,354 200,354" fill="var(--purple)"/>
    <polygon points="596,132 620,132 620,224 614,224" fill="var(--purple)"/>
    <line x1="196" y1="295" x2="616" y2="224" stroke="var(--red)" stroke-width="5"/>
    <line x1="596" y1="132" x2="616" y2="226" stroke="var(--red)" stroke-width="5"/>
  </svg>

  <div class="brand">
    <span class="brand-mark" aria-hidden="true"></span>
    <span class="brand-name">Fortivan</span>
  </div>
  <p class="brand-tagline">strength in every step</p>

  <ul class="contact-list">
    <li>
      <svg viewBox="0 0 12 12"><path d="M3 1l2 2-1 1.5c.6 1.4 1.6 2.4 3 3L8.5 6.5l2 2-1.5 2C5 10 2 7 1.5 2.5z" fill="var(--red)"/></svg>
      614.275.3081
    </li>
    <li>
      <svg viewBox="0 0 12 12"><rect x="1" y="3" width="10" height="7" fill="var(--red)"/><path d="M1 3l5 4 5-4" stroke="#fff" fill="none"/></svg>
      LVasquez@Fortivanco.example
    </li>
    <li>
      <svg viewBox="0 0 12 12"><circle cx="6" cy="6" r="5" fill="var(--red)"/><path d="M1 6h10M6 1c-2 3-2 7 0 10M6 1c2 3 2 7 0 10" stroke="#fff" stroke-width=".8" fill="none"/></svg>
      www.fortivanco.example
    </li>
  </ul>

  <div class="person">
    <p class="person-name">Lorena K. Vasquez</p>
    <p class="person-role">CEO</p>
  </div>

  <p class="coupon-note">Sign up on our website for a coupon code</p>

  <address class="address">
    P.O. Box 48317<br>
    Dayton, Ohio 22417
  </address>
</section>

<section class="card card-back" aria-label="Business card back">
  <div class="back-lockup">
    <p class="back-name">Fortivan</p>
    <p class="back-tagline">strength in every step</p>
  </div>
</section>

</body>
</html>
```